Website design and Setup for Real Estate Firm and Going Live

We are a commercial real estate investment firm and are looking for a 6 page website which is informational only. Some text and graphics on each page. We would want the designer to code and launch the website. This website needs to be corporate looking as well as innovative. We are setting up the website on hostivo.

The first page will be a home page with generic commercial real estate look with a link to the following 5 pages on page 1. So page one (the Home Page should have a commercial real estate look with the text linking to the following pages. Page 2 "About Us" with 3 paragraphs describing our firm. Page 3 "Our Platform" with another few paragraphs on due diligence, acquisitions, financing, and management.

Page 4 is "Our Team" highlighting several manager profiles. Page 5 is our "investment Portfolio portal" which will be password protected so not a lot of text, only general graphics and anyone viewing the site casually won't get into the backend, Page 6 is the contact us page. All of the content will be uploaded shortly.

The project includes setting up hyperlinks in the website as well rotating images etc and a final complete live online product. We do not expect to pay for any stock images.

Target Market(s)

Investors, Real Estate Professionals, Brokerages

Industry/Entity Type

Real Estate

Coding

Coded - Design and coding required

Number of Pages Required

5+ page

Requirements
Must have
• Corporate cutting edge design, suitable for a financial corporation.

```html
<!DOCTYPE html>
<html lang="en">
<head>
<meta charset="utf-8">
<title>Meridian Crest — Commercial Real Estate Investment Firm</title>
<link href="https://fonts.googleapis.com/css2?family=Cinzel:wght@400;600;700&family=EB+Garamond:wght@400;500&family=Lato:wght@400;700&display=swap" rel="stylesheet">
<style>
:root{
  --navy:#2a3a4b;
  --navy-deep:#223445;
  --steel:#1f4a66;
  --orange:#f7720f;
  --card:#f1f1f1;
  --ink:#1e1e1e;
  --text:#333;
  --white:#fff;
  --line:#8aa0b3;
}
*{margin:0;padding:0;box-sizing:border-box}
html,body{width:1200px;height:3953px;overflow:hidden}
body{font-family:'Lato',sans-serif;color:var(--text);background:var(--white);position:relative}
section,header,footer{position:absolute;left:0;width:1200px}
.abs{position:absolute}
.btn{position:absolute;display:flex;align-items:center;justify-content:center;background:var(--orange);color:var(--white);font-family:'Cinzel',serif;font-weight:700;font-size:12px;letter-spacing:.5px}
.heading{font-family:'Cinzel',serif;font-weight:700;font-size:36px;line-height:46px;color:var(--ink);letter-spacing:1px}

/* hero */
.hero{top:0;height:637px;overflow:hidden}
.hero-photo{position:absolute;inset:0;background:linear-gradient(180deg,#35c3ef 0%,#8fd8f0 22%,#d9d9d6 40%,#c9c4bd 60%,#8d8d8a 78%,#6f7a5c 88%,#b5b2ab 100%)}
.brand{position:absolute;left:72px;top:58px;font-family:'EB Garamond',serif;font-size:14px;color:#6c7580;letter-spacing:.5px}
.nav{position:absolute;right:75px;top:29px;display:flex;gap:28px;font-family:'EB Garamond',serif;font-size:18px;color:var(--ink)}
.nav .active{color:var(--orange)}
.hero-box{position:absolute;left:319px;top:155px;width:560px;height:221px;background:rgba(42,70,92,.82);color:var(--white);text-align:center;font-family:'Cinzel',serif}
.hero-box .l1{margin-top:22px;font-size:28px;letter-spacing:4px}
.hero-box .l2{font-size:54px;font-weight:700;letter-spacing:3px;line-height:64px}
.hero-box .l3{font-size:31px;letter-spacing:2px}
.hero-curve{position:absolute;left:0;bottom:0}

/* company */
.company{top:637px;height:449px}
.company-photo{left:84px;top:30px;width:507px;height:358px;background:radial-gradient(ellipse at 50% 40%,#d9d9d9 0%,#8c8c8c 45%,#ffffff 72%)}
.company .heading{left:612px;top:82px}
.company p{left:612px;top:179px;width:520px;font-size:15px;line-height:26px}

/* approach */
.approach{top:1086px;height:809px;background:var(--navy);color:var(--white)}
.approach .heading{color:var(--white);width:1200px;text-align:center;top:60px}
.approach .intro{top:126px;left:290px;width:620px;text-align:center;font-size:15px;line-height:26px}
.pillar{position:absolute;width:240px}
.pillar h3{font-size:19px;font-weight:700;line-height:26px;margin-bottom:10px}
.pillar p{font-size:14px;line-height:22px}
.pillar.left{left:79px;text-align:right}
.pillar.right{left:881px}
.center-mark{position:absolute;left:480px;top:290px;width:240px;text-align:center;font-family:'EB Garamond',serif;font-size:22px;color:#7d8792;letter-spacing:1px}

/* team */
.team{top:1895px;height:642px}
.team .heading{width:1200px;text-align:center;top:32px}
.card{position:absolute;top:166px;width:248px;height:382px;background:var(--card)}
.card .photo{height:167px}
.card .name{margin:18px 20px 0;font-size:17px;color:var(--ink)}
.card .role{margin:4px 20px 0;font-size:14px;color:#555}
.card .social{margin:10px 20px 0;display:flex;gap:7px}
.card .social span{width:8px;height:8px;border-radius:50%;background:var(--navy)}
.card p{margin:16px 20px 0;font-size:14px;line-height:22px;color:var(--text)}

/* portfolio */
.portfolio{top:2537px;height:374px;background:linear-gradient(90deg,#21475f 0%,#1f4d6b 55%,#2a5b7a 100%);overflow:hidden}
.portfolio .heading{color:var(--white);font-size:40px;line-height:50px;left:71px;top:80px}
.pw-field{left:71px;top:213px;width:488px;height:71px;border:4px solid var(--white)}
.pw-field .inner{position:absolute;left:4px;top:4px;right:4px;bottom:4px;background:var(--white)}
.pw-label{left:110px;top:199px;padding:0 10px;background:#21475f;color:var(--white);font-size:15px;line-height:22px}

/* contact */
.contact{top:2911px;height:488px}
.contact-form{left:71px;top:37px;width:529px;height:405px;background:var(--navy);color:var(--white)}
.contact-form .heading{color:var(--white);font-size:38px;left:66px;top:40px}
.field{position:absolute;border-bottom:1px solid var(--line);font-size:12px;height:20px}
.map{left:600px;top:37px;width:526px;height:405px;background:linear-gradient(135deg,#f1ece0 0%,#e6efdc 40%,#cfe3c9 65%,#efe9dc 100%)}

/* footer */
.footer{top:3399px;height:554px;background:var(--navy-deep);color:var(--white)}
.footer .brand{left:71px;top:170px;font-size:20px;color:#9aa4ae}
.footer .about{left:71px;top:238px;width:305px;font-size:13px;line-height:22px}
.col-title{position:absolute;top:112px;font-family:'EB Garamond',serif;font-size:16px;letter-spacing:1px}
.links{position:absolute;left:437px;top:141px;list-style:none;font-size:13px}
.links li{height:30px;padding-left:32px;position:relative}
.links li::before{content:"";position:absolute;left:2px;top:6px;width:6px;height:6px;border-radius:50%;background:var(--orange)}
.info{position:absolute;left:651px;font-size:13px;line-height:19px;padding-left:32px}
.info svg{position:absolute;left:0;top:2px}
.news{left:858px;top:141px;width:270px;font-size:13px;line-height:22px}
.news-input{left:858px;top:207px;width:270px;height:45px;background:var(--white);color:#444;font-size:13px;padding:14px 15px}
.rule{left:71px;top:413px;width:1058px;height:1px;background:#6d7d8c}
.socials{left:511px;top:396px;display:flex;gap:9px}
.socials span{width:34px;height:34px;border-radius:50%;background:var(--white);border:3px solid var(--navy-deep);outline:1px solid var(--white)}
.copy{top:462px;width:1200px;text-align:center;font-size:13px}
.copy b{color:var(--orange);font-weight:700}
</style>
</head>
<body>

<header class="hero">
  <div class="hero-photo" role="img" aria-label="Photo of a white commercial office building with parking lot under blue sky"></div>
  <div class="brand">MERIDIAN CREST</div>
  <nav class="nav">
    <span class="active">Home</span><span>Our Company</span><span>Investment Approach</span><span>Executive Team</span><span>Portfolio</span><span>Contact</span>
  </nav>
  <div class="hero-box">
    <div class="l1">COMMERCIAL</div>
    <div class="l2">REAL ESTATE</div>
    <div class="l3">INVESTMENT FIRM</div>
  </div>
  <div class="btn" style="left:540px;top:364px;width:120px;height:36px">CONTACT US</div>
  <svg class="hero-curve" width="1200" height="80" viewBox="0 0 1200 80"><path d="M0 80 L0 55 Q600 0 1200 55 L1200 80 Z" fill="#fff"/></svg>
</header>

<section class="company">
  <div class="abs company-photo" role="img" aria-label="Collage of tall glass towers rising from a curved base line"></div>
  <h2 class="abs heading">OUR<br>COMPANY</h2>
  <p class="abs">It is a long established fact that a reader will be distracted by the readable content of a page when looking at its layout. The point of using Lorem Ipsum is that it has a more-or-less normal distribution of letters,</p>
  <div class="btn" style="left:612px;top:278px;width:117px;height:36px">READ MORE</div>
</section>

<section class="approach">
  <h2 class="abs heading">INVESTMENT APPROACH</h2>
  <p class="abs intro">It is a long established fact that a reader will be distracted by the readable content of a page when looking at its layout.</p>
  <svg class="abs" style="left:0;top:0" width="1200" height="809" viewBox="0 0 1200 809">
    <circle cx="600" cy="367" r="230" fill="#fff" fill-opacity=".05"/>
    <circle cx="600" cy="367" r="138" fill="#fff" stroke="#2a3a4b" stroke-width="8"/>
    <circle cx="600" cy="367" r="138" fill="none" stroke="#fff" stroke-width="3"/>
    <g fill="#fff" stroke="#f7720f" stroke-width="4">
      <circle cx="382" cy="263" r="45"/><circle cx="816" cy="263" r="45"/>
      <circle cx="382" cy="461" r="45"/><circle cx="816" cy="461" r="45"/>
      <circle cx="600" cy="588" r="45"/>
    </g>
    <g fill="none" stroke="#222" stroke-width="2" stroke-linecap="round" stroke-linejoin="round">
      <!-- agreement -->
      <path d="M357 263 l12 -12 l14 6 l14 -6 l12 12 M369 251 l14 18 M383 257 l10 12 M372 272 l8 6 M380 270 l8 6"/>
      <!-- review -->
      <rect x="799" y="245" width="24" height="30" rx="2"/><path d="M804 253 h12 M804 259 h10"/><circle cx="823" cy="268" r="8"/><path d="M829 274 l8 8"/>
      <!-- holdings -->
      <path d="M368 452 l14 -9 l14 9 z M370 456 v14 M378 456 v14 M386 456 v14 M394 456 v14 M366 472 h32"/><path d="M362 462 v14 l8 8 M402 462 v14 l-8 8"/>
      <!-- funding -->
      <circle cx="820" cy="450" r="9"/><path d="M820 444 v12 M817 447 h5 a2 2 0 0 1 0 4 h-4 a2 2 0 0 0 0 4 h5"/><path d="M798 474 l10 -8 h12 l-4 5 h-8 M818 471 l14 -8 l3 4 l-14 12 h-18"/>
      <!-- oversight -->
      <rect x="586" y="570" width="24" height="32" rx="2"/><path d="M592 568 h12 v5 h-12 z M591 580 l2 2 l3 -3 M599 581 h7 M591 588 l2 2 l3 -3 M599 589 h5"/><circle cx="612" cy="596" r="5"/>
    </g>
  </svg>
  <div class="center-mark">MERIDIAN CREST</div>

  <div class="pillar left" style="top:204px"><h3>Trusted Partner –<br>Certainty of Execution</h3><p>It is a long established fact that a reader will be distracted by the readable content of a page</p></div>
  <div class="pillar right" style="top:230px"><h3>Due Diligence</h3><p>It is a long established fact that a reader will be distracted by the readable content of a page</p></div>
  <div class="pillar left" style="top:437px"><h3>Acquisitions</h3><p>It is a long established fact that a reader will be distracted by the readable content of a page</p></div>
  <div class="pillar right" style="top:437px"><h3>Financing</h3><p>It is a long established fact that a reader will be distracted by the readable content of a page</p></div>
  <div class="pillar" style="left:480px;top:653px;text-align:center"><h3>Management</h3><p>It is a long established fact that a reader will be distracted by the readable content of a page</p></div>
</section>

<section class="team">
  <h2 class="abs heading">OUR<br>EXECUTIVE TEAM</h2>
  <article class="card" style="left:71px">
    <div class="photo" role="img" aria-label="Portrait photo of team member" style="background:linear-gradient(180deg,#9db3bf,#6e7e86)"></div>
    <div class="name">Clara Benton</div><div class="role">Developer</div>
    <div class="social"><span></span><span></span><span></span></div>
    <p>It is a long established fact that a reader will be distracted page when looking at its layout.</p>
  </article>
  <article class="card" style="left:342px">
    <div class="photo" role="img" aria-label="Portrait photo of team member" style="background:linear-gradient(180deg,#d8d8d8,#9a9a9a)"></div>
    <div class="name">Dorian Vale</div><div class="role">Developer</div>
    <div class="social"><span></span><span></span><span></span></div>
    <p>It is a long established fact that a reader will be distracted page when looking at its layout.</p>
  </article>
  <article class="card" style="left:611px">
    <div class="photo" role="img" aria-label="Portrait photo of team member" style="background:linear-gradient(180deg,#7d8a99,#5b4d44)"></div>
    <div class="name">Nina Ashford</div><div class="role">Developer</div>
    <div class="social"><span></span><span></span><span></span></div>
    <p>It is a long established fact that a reader will be distracted page when looking at its layout.</p>
  </article>
  <article class="card" style="left:882px">
    <div class="photo" role="img" aria-label="Portrait photo of team member" style="background:linear-gradient(180deg,#efefef,#c9c9c9)"></div>
    <div class="name">Clara Benton</div><div class="role">Developer</div>
    <div class="social"><span></span><span></span><span></span></div>
    <p>It is a long established fact that a reader will be distracted page when looking at its layout.</p>
  </article>
  <div class="btn" style="left:540px;top:566px;width:120px;height:37px">VIEW ALL</div>
</section>

<section class="portfolio">
  <svg class="abs" style="left:0;top:0" width="1200" height="374" viewBox="0 0 1200 374" role="img" aria-label="Photo of a modern dark brick office building seen from below">
    <defs><linearGradient id="tower" x1="0" y1="0" x2="1" y2="1"><stop offset="0" stop-color="#4a5058"/><stop offset=".5" stop-color="#2f343b"/><stop offset="1" stop-color="#1c2026"/></linearGradient></defs>
    <polygon points="621,374 795,55 1200,110 1200,374" fill="url(#tower)"/>
  </svg>
  <h2 class="abs heading">INVESTMENT<br>PORTFOLIO</h2>
  <div class="abs pw-field"><div class="inner"></div>
    <svg class="abs" style="left:443px;top:24px" width="16" height="20" viewBox="0 0 16 20"><path d="M4 9 V6 a4 4 0 0 1 8 0 V9" fill="none" stroke="#222" stroke-width="2"/><rect x="2" y="9" width="12" height="10" rx="1" fill="#222"/><circle cx="8" cy="14" r="1.5" fill="#fff"/></svg>
  </div>
  <div class="abs pw-label">Enter Password</div>
</section>

<section class="contact">
  <div class="abs contact-form">
    <h2 class="abs heading">CONTACT US</h2>
    <div class="field" style="left:67px;top:125px;width:180px">Full Name *</div>
    <div class="field" style="left:257px;top:125px;width:180px">Email *</div>
    <div class="field" style="left:67px;top:174px;width:180px">Phone Number*</div>
    <div class="field" style="left:257px;top:174px;width:180px">Country *</div>
    <div class="field" style="left:67px;top:221px;width:376px">Company*</div>
    <div class="field" style="left:67px;top:269px;width:376px">Message *</div>
    <div class="btn" style="left:67px;top:316px;width:118px;height:35px">SUBMIT NOW</div>
  </div>
  <div class="abs map" role="img" aria-label="Map showing the office location"></div>
</section>

<footer class="footer">
  <div class="abs brand">MERIDIAN CREST</div>
  <p class="abs about">It is a long established fact that a reader will be distracted by the readable content of a page when looking at its layout.The point of using Lorem Ipsum is that it has a more-or-less normal distribution of letters,</p>

  <div class="col-title" style="left:437px">QUICK LINK</div>
  <ul class="links"><li>Home</li><li>Our Company</li><li>Investment Approach</li><li>Executive Team</li><li>Portfolio</li><li>Contact</li></ul>

  <div class="col-title" style="left:651px">CONTACT US</div>
  <div class="info" style="top:141px">
    <svg width="12" height="16" viewBox="0 0 12 16"><path d="M6 0 a6 6 0 0 1 6 6 c0 4 -6 10 -6 10 S0 10 0 6 a6 6 0 0 1 6 -6z" fill="#fff"/><circle cx="6" cy="6" r="2.2" fill="#223445"/></svg>
    Suite 14b<br>Harbor Point Plaza<br>72 Linden Avenue,
  </div>
  <div class="info" style="top:222px">
    <svg width="14" height="14" viewBox="0 0 14 14"><path d="M3 0 l3 3 l-2 2 a8 8 0 0 0 5 5 l2 -2 l3 3 l-2 3 C6 14 0 8 0 3z" fill="#fff"/></svg>
    555-014-0261
  </div>
  <div class="info" style="top:256px">
    <svg width="14" height="10" viewBox="0 0 14 10"><rect width="14" height="10" fill="#fff"/><path d="M0 0 l7 6 l7 -6" fill="none" stroke="#223445" stroke-width="1.5"/></svg>
    hello@meridiancrest.com
  </div>

  <div class="col-title" style="left:858px">NEWSLETTER</div>
  <p class="abs news">Lorem Ipsum is simply dummy text of the printing and typesetting industry.</p>
  <div class="abs news-input">Enter Your Mail ID</div>
  <div class="btn" style="left:858px;top:259px;width:118px;height:37px">SUBMIT NOW</div>

  <div class="abs rule"></div>
  <div class="abs socials"><span></span><span></span><span></span><span></span></div>
  <p class="abs copy">© 2021 <b>meridiancrest</b> All rights reserved.</p>
</footer>

</body>
</html>
```